BRIGHTDESK - Remote Tech Support Site

We are looking for a new very responsive and simple website for our brand Brightdesk.com - a remote technical support company.

This company supports customers Globally in different countries throughout Eur/ North America / South America / Asia etc (please keep this in mind and integrate into the idea).

Its important to us that the design is very explanatory, the customer should easily be able to figure out that we provide computer support right away ... I like one page responsive type designs as well without a bunch of menu items

Here are some similar sites we like - but still looking for a unique design that fits out brand "brightdesk" - I have upload also some layouts i like (but the designs are not important just the layouts), youll see it includes consumer business etc which is important.

VOLM.COM - I love how clean it is - nice and white easy to see everything

PLUMWIRE247.COM - also nice the layout and responsive one page design makes it easy to use

corvalfix.com - similar to plumwire design as well - you can get the idea im looking for between the two

You will notice those examples are much different then the attachments I added - again this is more of an idea for possible layouts .. attached is also the logo - could inspire color scheme / blue white black etc

Target Market(s)

Home consumers without computer knowledge , older age 45-65, small medium business ... computer repair - slow computers

Industry/Entity Type

Computer Repair

Logo Text

Brightdesk

Coding

Coded - Design and coding required

Number of Pages Required

1 page

Font styles to use
Sans Serif
Other font styles liked:
• your choice responsive

Colors

Designer to choose colors to be used in the design.

Requirements
Must have
• Clean - responsive - professional design - the name says it all - brightdesk
• CALL TO ACTIONS FOR "Get Help Now!" / "Learn More" etc
Nice to have
• We are looking for a new very responsive and simple website for our brand Brightdesk.com - a remote technical support company.
• This company supports customers Globally in different countries throughout Eur/ North America / South America / Asia etc (please keep this in mind and integrate into the idea).
• Its important to us that the design is very explanatory, the customer should easily be able to figure out that we provide computer support right away ... I like one page responsive type designs as well without a bunch of menu items
• Here are some similar sites we like - but still looking for a unique design that fits out brand "brightdesk" - I have upload also some layouts i like (but the designs are not important just the layouts), youll see it includes consumer business etc which is important.
• VOLM.COM - I love how clean it is - nice and white easy to see everything
• PLUMWIRE247.COM - also nice the layout and responsive one page design makes it easy to use
• corvalfix.com - similar to plumwire design as well - you can get the idea im looking for between the two
Should not have
• dark, packed page - bad small font -

```html
<!DOCTYPE html>
<html lang="en">
<head>
<meta charset="utf-8">
<title>Brightdesk – Remote Tech Support</title>
<link href="https://fonts.googleapis.com/css2?family=Open+Sans:wght@400;600;700;800&display=swap" rel="stylesheet">
<style>
:root{
  --blue:#1a8fe3;
  --blue-deep:#1565c0;
  --blue-band:#2b8cf0;
  --black:#0b0b0b;
  --dark:#1b1b1b;
  --grey-band:#3b3d40;
  --text:#333;
  --muted:#666;
  --light:#f2f4f6;
  --white:#fff;
  --yellow:#ffd200;
  --orange:#f57c00;
  --green:#1e9e35;
}
*{box-sizing:border-box;margin:0;padding:0}
html,body{width:1200px;height:4891px;overflow:hidden}
body{font-family:"Open Sans",Arial,sans-serif;color:var(--text);background:var(--white);position:relative}
section,header,footer{position:absolute;left:0;width:1200px}
.abs{position:absolute}
.section-icon{position:absolute;left:570px;width:60px;height:60px;border-radius:50%;background:var(--blue);border:4px solid var(--white);box-shadow:0 0 0 2px var(--blue)}
.section-title{position:absolute;left:0;width:1200px;text-align:center;font-weight:700;color:var(--blue);text-transform:uppercase}
.lead{position:absolute;left:200px;width:800px;text-align:center;font-size:16px;line-height:24px}

/* header */
.site-header{top:0;height:91px;background:var(--black)}
.brand{position:absolute;left:170px;top:24px;display:flex;align-items:center;gap:10px;color:var(--white);font-weight:700;font-size:28px}
.brand-dot{width:36px;height:36px;border-radius:50%;background:var(--blue)}
.locale{position:absolute;left:845px;top:4px;font-size:14px;color:var(--blue);font-weight:600}
.main-nav{position:absolute;left:595px;top:42px;display:flex;gap:22px;font-size:16px;color:var(--white)}
.main-nav .active{color:var(--blue);border-bottom:2px solid var(--blue);padding-bottom:4px}

/* hero */
.hero{top:91px;height:457px}
.hero-photo{position:absolute;inset:0;background:linear-gradient(90deg,#7d8c99 0%,#c9d0d6 22%,#9a7fc2 40%,#e6e2ee 55%,#b9c7d2 72%,#3c3f41 88%,#2d2f31 100%)}
.hero-strip{position:absolute;left:280px;top:180px;width:640px;height:100px;background:rgba(255,255,255,.85)}
.hero-tagline{position:absolute;left:0;top:200px;width:1200px;text-align:center;font-size:44px;font-weight:600;color:#9a9a9a}
.contact-tab{position:absolute;right:0;top:18px;width:160px;height:40px;background:var(--black);border-radius:20px 0 0 20px;color:var(--white);font-size:15px;line-height:40px;padding-left:38px;letter-spacing:1px}
.slider-arrow{position:absolute;left:8px;top:210px;width:34px;height:40px;background:rgba(0,0,0,.55)}

/* welcome */
.welcome{top:548px;height:218px}
.welcome h2{top:82px;font-size:27px;text-transform:none;font-weight:600}
.welcome h2 b{font-weight:800}

/* quick band */
.quick-band{top:766px;height:186px;background:var(--grey-band);color:var(--white)}
.quick-item{position:absolute;top:0;height:186px;padding:18px 12px}
.quick-item h3{font-size:27px;font-weight:400;line-height:32px}
.quick-item p{font-size:15px;line-height:20px;margin-top:6px;color:#e0e0e0}
.quick-item.highlight{background:var(--blue-deep)}

/* pricing */
.pricing{top:952px;height:515px;background:var(--light)}
.pricing h2{top:95px;font-size:33px}
.plan{position:absolute;top:228px;width:244px;height:254px;background:var(--white);box-shadow:0 2px 6px rgba(0,0,0,.2);text-align:center}
.plan-head{height:98px;color:var(--white);padding-top:10px}
.plan-head h3{font-size:22px;font-weight:800}
.plan-head .price{font-size:18px;font-weight:700}
.plan-head .price small{font-size:11px}
.plan-head .fee{font-size:13px;font-weight:700;color:#ffe9c8}
.plan-body{padding:20px 20px 0;font-size:12px;line-height:18px;color:#333}
.plan-body b{font-weight:700}
.plan-link{position:absolute;bottom:8px;left:0;width:100%;font-size:10px;letter-spacing:2px;color:#666}
.plan.green .plan-head{background:var(--green)}
.plan.blue .plan-head{background:var(--blue)}
.plan.orange .plan-head{background:var(--orange)}

/* why */
.why{top:1467px;height:652px;background:var(--black);color:var(--white)}
.why h2{top:100px;font-size:34px}
.reason{position:absolute;width:470px}
.reason h3{color:var(--blue);font-size:21px;font-weight:600}
.reason p{font-size:16px;line-height:22px;color:#e6e6e6;margin-top:4px}
.devices{position:absolute;left:260px;top:408px;width:685px;height:244px;background:linear-gradient(180deg,#5d6b80,#1f2a3a 70%,#0b0b0b)}

/* features */
.features{top:2119px;height:805px;background:linear-gradient(180deg,#f4f6f8,#e8eef3 50%,#fdfdfd)}
.features h2{top:96px;font-size:34px}
.feature{position:absolute;width:215px;text-align:center}
.feature svg{display:block;margin:0 auto}
.feature h3{color:var(--blue);font-size:17px;font-weight:700;margin-top:10px}
.feature p{font-size:14px;line-height:19px;color:#444}

/* advisors */
.advisors{top:2924px;height:721px;background:linear-gradient(90deg,#9cc7f0 0%,var(--blue-band) 35%,var(--blue-band) 100%);color:var(--white)}
.advisors h2{top:118px;font-size:34px;color:var(--white)}
.advisor{position:absolute;width:420px}
.advisor h3{color:var(--yellow);font-size:22px;font-weight:700}
.advisor p{font-size:16px;line-height:20px;margin-top:2px}

/* consult */
.consult{top:3645px;height:593px;background:var(--white)}
.world-map{position:absolute;left:170px;top:40px;width:860px;height:250px;background:radial-gradient(ellipse at center,#e4e7ea,rgba(255,255,255,0) 70%)}
.skyline{position:absolute;left:0;top:340px;width:1200px;height:253px;background:linear-gradient(180deg,rgba(255,255,255,0),#9a9a9a 55%,#3a3a3a)}
.consult h2{top:140px;font-size:32px;line-height:42px}
.video{position:absolute;left:342px;top:235px;width:522px;height:260px;background:linear-gradient(180deg,#333,#111);border:3px solid #222}

/* offer */
.offer{top:4238px;height:310px;background:var(--white)}
.offer h2{top:50px;font-size:30px;color:var(--black)}
.offer-form{position:absolute;left:156px;top:108px;width:888px;display:grid;grid-template-columns:repeat(3,1fr);row-gap:12px;column-gap:8px}
.offer-form span{display:block;height:52px;border:1px solid #bbb;font-size:13px;padding:15px 10px;color:#444}
.cta{position:absolute;left:528px;top:262px;width:146px;height:38px;background:var(--orange);color:var(--white);font-size:15px;font-weight:600;text-align:center;line-height:38px}

/* footer */
.site-footer{top:4548px;height:343px;background:var(--black);color:var(--white);border-top:4px solid var(--orange)}
.footer-brand{position:absolute;left:173px;top:28px;display:flex;align-items:center;gap:8px;font-weight:700;font-size:20px}
.footer-brand span{width:22px;height:22px;border-radius:50%;background:var(--blue)}
.footer-about{position:absolute;left:173px;top:80px;width:260px;font-size:16px;line-height:28px}
.follow{position:absolute;left:173px;top:205px;font-size:16px;font-weight:700;display:flex;align-items:center;gap:10px}
.follow i{width:28px;height:28px;border:2px solid #fff;border-radius:50%}
.call{position:absolute;left:173px;top:240px;color:var(--blue);font-size:18px;font-weight:700}
.mail{position:absolute;left:466px;top:240px;color:var(--blue);font-size:16px;font-weight:600}
.footer-col h4{font-size:22px;font-weight:700}
.footer-col ul{list-style:none;font-size:16px;line-height:26px;margin-top:8px}
.news p{font-size:16px;line-height:22px;margin-top:8px;width:360px}
.news-input{position:absolute;top:118px;left:0;width:240px;height:36px;background:var(--white);color:#888;font-size:14px;padding:8px 10px}
.news-btn{position:absolute;top:118px;left:250px;width:100px;height:36px;background:var(--orange);font-weight:700;font-size:15px;text-align:center;line-height:36px}
.badge{position:absolute;top:215px;height:44px;background:#5a5a5a;border-radius:4px}
.copyright{position:absolute;left:0;top:318px;width:1200px;text-align:center;font-size:10px;color:#aaa}
</style>
</head>
<body>

<header class="site-header">
  <div class="brand"><span class="brand-dot"></span>brightdesk</div>
  <div class="locale">United States - EN &nbsp;|&nbsp; Login</div>
  <nav class="main-nav"><span class="active">Home</span><span>About Us</span><span>Services</span><span>Contact Us</span><span>Faqs</span></nav>
</header>

<section class="hero">
  <div class="hero-photo" role="img" aria-label="Photo collage of support technicians, a data privacy keyboard and a chalkboard reading We focus on quality"></div>
  <div class="hero-strip"></div>
  <div class="hero-tagline">Your potential. Our passion.</div>
  <div class="contact-tab">Contact Us</div>
  <div class="slider-arrow"><svg width="34" height="40"><path d="M20 12l-8 8 8 8" stroke="#fff" stroke-width="3" fill="none"/></svg></div>
</section>

<section class="welcome">
  <div class="section-icon" style="top:18px"></div>
  <h2 class="section-title">Welcome to <b>BRIGHTDESK</b></h2>
  <p class="lead" style="top:128px">We are a group of technicians who work round the clock to ensure that your PC works perfectly. Get your computer free of suspicious software and have a healthy system</p>
</section>

<section class="quick-band">
  <div class="quick-item" style="left:170px;width:220px"><h3>FREE<br>Diagnostic</h3><p>Get a diagnostic, FOR FREE! Get a free consultation with our staff</p></div>
  <div class="quick-item highlight" style="left:391px;width:365px;padding-left:20px"><h3>Backup your<br>information!</h3><p>Saving your files is now EASY!<br>You will be able to retain your personal files without any loss of data</p></div>
  <div class="quick-item" style="left:780px;width:260px"><h3>Get<br>Fixed</h3><p>Get fixed, IMMEDIATELY!<br>Our staff will solve your computer issues right before your eyes</p></div>
  <svg class="abs" style="left:975px;top:70px" width="44" height="52" viewBox="0 0 44 52"><path d="M22 3L5 10v14c0 12 8 21 17 25 9-4 17-13 17-25V10z" fill="none" stroke="#5fb3ff" stroke-width="4"/></svg>
</section>

<section class="pricing">
  <div class="section-icon" style="top:38px"></div>
  <h2 class="section-title">Membership Pricing and Plans</h2>
  <p class="lead" style="top:140px;left:240px;width:720px">Lorem Ipsum is simply dummy text of the printing and typesetting industry. Lorem Ipsum has been the industry's standard dummy text ever since the 1500s</p>
  <div class="plan green" style="left:212px">
    <div class="plan-head"><h3>PREMIUM</h3><div class="price">$19.99 <small>/MONTHLY</small></div><div class="fee">($249-$300 setup fee)</div></div>
    <div class="plan-body">Regular 90-Day Optimization<br><b>Unlimited 24/7 Tier 3 Technician Support</b></div>
    <div class="plan-link">LEARN MORE</div>
  </div>
  <div class="plan blue" style="left:489px">
    <div class="plan-head"><h3>PREMIUM PLUS</h3><div class="price">$29.99 <small>/MONTHLY</small></div><div class="fee">($249-$300 setup fee)</div></div>
    <div class="plan-body">Regular 90-Day Optimization<br><b>Unlimited 24/7 Tier 3 Technician Support</b></div>
    <div class="plan-link">LEARN MORE</div>
  </div>
  <div class="plan orange" style="left:766px">
    <div class="plan-head"><h3>PLATINUM</h3><div class="price">$39.99 <small>/MONTHLY</small></div><div class="fee">($249-$300 setup fee)</div></div>
    <div class="plan-body">Regular 90-Day Optimization<br><b>Unlimited 24/7 Tier 3 Technician Support</b><br>Online Identity Theft Protection</div>
    <div class="plan-link">LEARN MORE</div>
  </div>
</section>

<section class="why">
  <div class="section-icon" style="top:22px"></div>
  <h2 class="section-title">Why Join Us</h2>
  <div class="reason" style="left:173px;top:170px"><h3>Best reviews in the entire industry</h3><p>Lorem Ipsum is simply dummy text of the printing and typesetting industry.</p></div>
  <div class="reason" style="left:675px;top:170px"><h3>Exceptional Service &amp; Guarantee</h3><p>Lorem Ipsum is simply dummy text of the printing and typesetting industry.</p></div>
  <div class="reason" style="left:173px;top:290px"><h3>Experience and Expert IT Technicians</h3><p>Lorem Ipsum is simply dummy text of the printing and typesetting industry.</p></div>
  <div class="reason" style="left:675px;top:290px"><h3>Best Technology and Partners</h3><p>Lorem Ipsum is simply dummy text of the printing and typesetting industry.</p></div>
  <div class="devices" role="img" aria-label="Laptop, tablets and phones showing the support software across devices"></div>
</section>

<section class="features">
  <div class="section-icon" style="top:20px"></div>
  <h2 class="section-title">All the best features, at the best price!</h2>
  <p class="lead" style="top:138px;left:210px;width:780px">Lorem Ipsum is simply dummy text of the printing and typesetting industry. Lorem Ipsum has been the industry's standard dummy text ever since the 1500s</p>

  <div class="feature" style="left:183px;top:215px">
    <svg width="150" height="150"><circle cx="75" cy="75" r="64" fill="#eef1f4" stroke="#dfe3e7" stroke-width="12"/><path d="M75 11A64 64 0 0 1 139 75" fill="none" stroke="#1a8fe3" stroke-width="12"/><rect x="58" y="58" width="34" height="34" rx="4" fill="#9aa7b3"/></svg>
    <h3>Ad Blocker</h3><p>Avoid unwanted Pop-ups with the newest Ad Blocking technology.</p></div>
  <div class="feature" style="left:398px;top:215px">
    <svg width="150" height="150"><circle cx="75" cy="75" r="64" fill="#eef1f4" stroke="#dfe3e7" stroke-width="12"/><path d="M75 11A64 64 0 0 1 139 75" fill="none" stroke="#1a8fe3" stroke-width="12"/><rect x="52" y="60" width="46" height="30" rx="3" fill="#9aa7b3"/></svg>
    <h3>Regular Tune-Ups</h3><p>Get a Regular Tune-Up and Optimization every 90-days.</p></div>
  <div class="feature" style="left:607px;top:215px">
    <svg width="150" height="150"><circle cx="75" cy="75" r="64" fill="#eef1f4" stroke="#dfe3e7" stroke-width="12"/><path d="M75 11A64 64 0 0 1 139 75" fill="none" stroke="#1a8fe3" stroke-width="12"/><rect x="60" y="54" width="30" height="40" rx="3" fill="#9aa7b3"/></svg>
    <h3>System Reports</h3><p>Stay up to date with Real-Time System Reporting.</p></div>
  <div class="feature" style="left:822px;top:215px">
    <svg width="150" height="150"><circle cx="75" cy="75" r="64" fill="#eef1f4" stroke="#dfe3e7" stroke-width="12"/><path d="M75 11A64 64 0 0 1 139 75" fill="none" stroke="#1a8fe3" stroke-width="12"/><rect x="54" y="58" width="24" height="20" fill="#9aa7b3"/><rect x="74" y="74" width="22" height="18" fill="#1a8fe3"/></svg>
    <h3>Multiple Devices</h3><p>Get support for up to 4 multiple devices. Ask about our Family Plans.</p></div>

  <div class="feature" style="left:183px;top:515px">
    <svg width="150" height="150"><circle cx="75" cy="75" r="64" fill="#eef1f4" stroke="#dfe3e7" stroke-width="12"/><rect x="58" y="56" width="34" height="38" rx="4" fill="#9aa7b3"/></svg>
    <h3>Identity Protection</h3><p>Coming Soon.</p></div>
  <div class="feature" style="left:398px;top:515px">
    <svg width="150" height="150"><circle cx="75" cy="75" r="64" fill="#eef1f4" stroke="#dfe3e7" stroke-width="12"/><rect x="63" y="50" width="24" height="46" rx="4" fill="#1a8fe3"/></svg>
    <h3>Mobile Security</h3><p>Coming Soon.</p></div>
  <div class="feature" style="left:607px;top:515px">
    <svg width="150" height="150"><circle cx="75" cy="75" r="64" fill="#eef1f4" stroke="#dfe3e7" stroke-width="12"/><path d="M75 11A64 64 0 0 1 139 75" fill="none" stroke="#1a8fe3" stroke-width="12"/><rect x="54" y="58" width="40" height="28" rx="3" fill="#9aa7b3"/></svg>
    <h3>Cross Platform</h3><p>One Support Plan for different types of devices.</p></div>
  <div class="feature" style="left:822px;top:515px">
    <svg width="150" height="150"><circle cx="75" cy="75" r="64" fill="#eef1f4" stroke="#dfe3e7" stroke-width="12"/><path d="M58 88h36a12 12 0 0 0-2-24 16 16 0 0 0-30 4 10 10 0 0 0-4 20z" fill="none" stroke="#7a8793" stroke-width="4"/></svg>
    <h3>Cloud Backup</h3><p>Keep your data safe! Ask about our plans for Unlimited Cloud Backup.</p></div>
</section>

<section class="advisors">
  <div class="abs" style="left:0;top:0;width:520px;height:721px;background:linear-gradient(90deg,rgba(230,240,250,.6),rgba(43,140,240,0))" role="img" aria-label="Support advisor with headset working at a desk"></div>
  <div class="section-icon" style="top:36px"></div>
  <h2 class="section-title">Expert Advisors</h2>
  <div class="advisor" style="left:173px;top:205px"><h3>Consumer business</h3><p>Lorem Ipsum is simply dummy text of the printing and typesetting industry. Lorem Ipsum has been the industry's standard dummy text ever since the 1500s</p></div>
  <div class="advisor" style="left:636px;top:205px"><h3>24/7 Support</h3><p>Lorem Ipsum is simply dummy text of the printing and typesetting industry. Lorem Ipsum has been the industry's standard dummy text ever since the 1500s</p></div>
  <div class="advisor" style="left:173px;top:360px"><h3>Business computer service</h3><p>Lorem Ipsum is simply dummy text of the printing and typesetting industry. Lorem Ipsum has been the industry's standard dummy text ever since the 1500s</p></div>
  <div class="advisor" style="left:636px;top:360px"><h3>Diagnosis, repair &amp; tune-up</h3><p>Lorem Ipsum is simply dummy text of the printing and typesetting industry. Lorem Ipsum has been the industry's standard dummy text ever since the 1500s</p></div>
  <div class="advisor" style="left:173px;top:515px"><h3>Instant help</h3><p>Lorem Ipsum is simply dummy text of the printing and typesetting industry. Lorem Ipsum has been the industry's standard dummy text ever since the 1500s</p></div>
  <div class="advisor" style="left:636px;top:515px"><h3>Personal IT Supporter</h3><p>Lorem Ipsum is simply dummy text of the printing and typesetting industry. Lorem Ipsum has been the industry's standard dummy text ever since the 1500s</p></div>
</section>

<section class="consult">
  <div class="world-map" role="img" aria-label="Faint world map showing global coverage"></div>
  <div class="skyline" role="img" aria-label="City skyline silhouette"></div>
  <div class="section-icon" style="top:60px"></div>
  <h2 class="section-title">Get a 30-minute one-on-one free<br>consultation with one of our experts!</h2>
  <div class="video" role="img" aria-label="Introductory video of a support session">
    <svg class="abs" style="left:221px;top:90px" width="80" height="80"><circle cx="40" cy="40" r="36" fill="none" stroke="#fff" stroke-width="4"/><path d="M32 24l22 16-22 16z" fill="#fff"/></svg>
  </div>
</section>

<section class="offer">
  <h2 class="section-title">Request your personal offer now!</h2>
  <div class="offer-form">
    <span>Name</span><span>Email</span><span>Telephone Number</span>
    <span>City</span><span>State</span><span>Pin</span>
  </div>
  <div class="cta">Get Help Now!</div>
</section>

<footer class="site-footer">
  <div class="footer-brand"><span></span>brightdesk</div>
  <p class="footer-about">You can get in touch with us any time of the day, any day of the week. We offer support through phone and online chat.</p>
  <div class="follow">Follow Us : <i></i><i></i></div>
  <div class="call">CALL US : (888) 555-0142</div>
  <div class="mail">info@brightdesk.com</div>
  <div class="footer-col abs" style="left:483px;top:28px"><h4>PLANS</h4><ul><li>Premium Plan</li><li>Premium Plus Plan</li><li>Platinum Plan</li></ul></div>
  <div class="footer-col news abs" style="left:684px;top:28px;width:380px;height:270px"><h4>NEWSLETTER SIGNUP</h4><p>Sign up for our regular informational newsletters</p>
    <div class="news-input">e-mail</div><div class="news-btn">SIGN UP</div>
    <div class="badge" style="left:0;width:80px"></div>
    <div class="badge" style="left:90px;width:90px;border-radius:22px"></div>
    <div class="badge" style="left:190px;width:44px;border-radius:50%;background:#8a7a3a"></div>
  </div>
  <div class="copyright">Brightdesk Ltd 2014. All rights reserved. &nbsp;Terms and Conditions · Refund Policy · Privacy Policy</div>
</footer>

</body>
</html>
```